Buch-/E-Book-Cover für ein Lernbuch
Vielen Dank für die ausgezeichnete Arbeit! Gerne wieder! kreativ7
Zielgruppe
Ich biete Lerncoachings und Prüfungscoaching für Schüler und Studenten an.
Meine Zielgruppe sind Schüler von 12-18 Jahren und Eltern und erziehungsberechtigte Personen.
Aufgabenstellung
Ich benötige ein ansprechendes Buch-Cover. Das Format für das Buch ist 15,24 x 22,86 cm (6' x 9').
Mein Buch Cover soll sich aber deutlich von den anderen Büchern abheben und Jugendliche (keine Kinder) ansprechen.
Wichtig ist mir auch einen Wiedererkennungswert vom Buch-Cover zu haben.
Bitte um ein ansprechendes Bild, denn ich möchte mich deutlich von meiner Konkurrenz abheben.
Autoren: Birgit Wendler und Helga Wendler
Titel: Die Reise durch das bunte Heftland am frühen Morgen
Untertitel: Entspanntes zügiges Büffeln für Jugendliche
Buchrücken
Lernen ist nicht gleich Lernen. Was ist Lernen und welche Lernmethoden sind erfolgreich? Das sind die Fragen, die dieses Buch beantwortet.
Warum ist es wichtig zu lernen, wie man lernt? Lernen ist ein wichtiger Prozess für Kinder und Schüler. Sie verbringen viel Zeit damit, neues Wissen aufzunehmen, und es hört nie auf. Denn wir lernen fürs Leben – lebenslanges Lernen. Wir lernen laufen, wir lernen sprechen, wir lernen rechnen und so weiter. Lernen begleitet uns ein Leben lang. Das Auswendiglernen von neuem Wissen ist sehr wichtig, und die richtigen Lernmethoden sind dabei sehr hilfreich. Die notwendige Struktur kann durch entsprechende Lernpläne erreicht werden, die unter Berücksichtigung von Lernorganisation und Zeitmanagement erstellt werden.
Um schnell und erfolgreich zu lernen, braucht es die richtigen Lernmethoden.
Eines ist dabei immer wichtig: Lernen darf und soll Spaß machen und Lernen kann stressfrei sein. Jeder kann lernen zu lernen. In diesem Buch zeigen wir, wie unterschiedliche Lerntypen und unterschiedliche Lernmethoden zum gewünschten Schulerfolg führen.
Mein Name ist Birgit Wendler und gemeinsam mit meiner Mutter Helga Wendler haben wir dieses Buch geschrieben. Sie profitieren in diesem Buch von der langjährigen Erfahrung meiner Mutter Helga Wendler, die über 40 Jahre als Lehrerin in einer Mittelschule tätig war, u..

```html
<!DOCTYPE html>
<html lang="de">
<head>
<meta charset="utf-8">
<title>Buchrücken – Lernbuch</title>
<link rel="stylesheet" href="https://fonts.googleapis.com/css2?family=Courier+Prime&display=swap">
<style>
  :root {
    --cover-orange: #f5861f;
    --ink: #141210;
  }
  html, body {
    margin: 0;
    padding: 0;
    width: 768px;
    height: 1200px;
    overflow: hidden;
    background: var(--cover-orange);
  }
  .back-cover {
    position: relative;
    width: 768px;
    height: 1200px;
    background: var(--cover-orange);
    box-sizing: border-box;
    padding: 66px 33px 0 33px;
  }
  .blurb {
    font-family: "Courier Prime", "Courier New", monospace;
    font-size: 20.4px;
    line-height: 31.5px;
    color: var(--ink);
    text-align: justify;
    hyphens: none;
  }
  .blurb p {
    margin: 0 0 24px 0;
  }
</style>
</head>
<body>
  <main class="back-cover">
    <section class="blurb">
      <p>Lernen ist nicht gleich Lernen. Was ist Lernen und welche Lernmethoden sind erfolgreich? Das sind die Fragen, die dieses Buch beantwortet.</p>
      <p>Warum ist es wichtig zu lernen, wie man lernt? Lernen ist ein wichtiger Prozess für Kinder und Schüler. Sie verbringen viel Zeit damit, neues Wissen aufzunehmen, und es hört nie auf. Denn wir lernen fürs Leben – lebenslanges Lernen. Wir lernen laufen, wir lernen sprechen, wir lernen rechnen und so weiter. Lernen begleitet uns ein Leben lang. Das Auswendiglernen von neuem Wissen ist sehr wichtig, und die richtigen Lernmethoden sind dabei sehr hilfreich. Die notwendige Struktur kann durch entsprechende Lernpläne erreicht werden, die unter Berücksichtigung von Lernorganisation und Zeitmanagement erstellt werden.<br>Um schnell und erfolgreich zu lernen, braucht es die richtigen Lernmethoden.</p>
      <p>Eines ist dabei immer wichtig: Lernen darf und soll Spaß machen und Lernen kann stressfrei sein. Jeder kann lernen zu lernen. In diesem Buch zeigen wir, wie unterschiedliche Lerntypen und unterschiedliche Lernmethoden zum gewünschten Schulerfolg führen.</p>
      <p>Mein Name ist Birgit Wendler und gemeinsam mit meiner Mutter Helga Wendler haben wir dieses Buch geschrieben. Sie profitieren in diesem Buch von der langjährigen Erfahrung meiner Mutter Helga Wendler, die über 40 Jahre als Lehrerin in einer Mittelschule tätig war, und von meinen Erfahrungen.</p>
    </section>
  </main>
</body>
</html>
```